Web App UI Design prototype

I have a sketch of a series of pages for a new web app, and would like to develop a clean, user friendly, intuitive design around the content.

Target Market(s)

small to medium sized business owners

Number of Pages Required

5+ page

Font styles to use
Sans Serif

Colors
33a6d7
85cae6
33b8a4
86cfc6
886aae
faa54b
000000
757575
cbcbcb

Requirements
Must have
• Color pallet that fits with my logo
• Clean modern, timeless design
• Intuitive use of UI
• Icons always help

```html
<!DOCTYPE html>
<html lang="en">
<head>
<meta charset="utf-8">
<title>Kelvo – Dashboard</title>
<link rel="stylesheet" href="https://fonts.googleapis.com/css2?family=Roboto:wght@300;400;500;700&display=swap">
<style>
:root{
  --brand-green:#3d8b35;
  --brand-blue:#06a9e0;
  --run-blue:#14a6dd;
  --logo-blue:#23b3e2;
  --text-dark:#333333;
  --text-mid:#5f5f5f;
  --line:#dcdcdc;
  --filter-bg:#f0f0f0;
  --footer:#000000;
  --white:#ffffff;
  --chart-blue:#1f77b4;
  --chart-orange:#ff7f0e;
  --pie-blue:#4e80c2;
  --pie-purple:#8a63b0;
  --line-red:#f07b7b;
  --line-teal:#27b3a3;
}
*{box-sizing:border-box;margin:0;padding:0}
html,body{width:1200px;height:643px;overflow:hidden;font-family:"Roboto",Arial,sans-serif;background:var(--white);color:var(--text-dark)}
.app{position:relative;width:1200px;height:643px}
.sidebar{position:absolute;left:0;top:0;width:188px;height:495px;border-right:1px solid var(--line);background:var(--white)}
.brand{height:103px;display:flex;align-items:center;padding-left:12px;gap:10px}
.brand-mark{width:14px;height:14px;border-radius:50%;background:var(--logo-blue)}
.brand-name{font-size:42px;font-weight:300;color:var(--logo-blue);letter-spacing:1px}
.run-btn{position:absolute;left:28px;top:107px;width:131px;height:46px;background:var(--run-blue);border-radius:3px;display:flex;align-items:center;justify-content:center;gap:18px;color:var(--white);font-size:18px;font-weight:500}
.nav{position:absolute;top:158px;left:0;width:188px}
.nav-item{height:42px;display:flex;align-items:center;justify-content:flex-end;gap:10px;padding-right:16px;font-size:13.5px;font-weight:500;color:var(--white);background:var(--brand-blue);border-bottom:1px solid rgba(255,255,255,.55)}
.nav-item.group{background:var(--white);color:var(--text-mid);font-weight:400;font-size:14.5px;padding-right:14px;border-bottom:1px solid var(--line)}
.nav-item svg{flex:none}
.topbar{position:absolute;left:188px;top:0;width:1012px;height:89px;background:var(--brand-green);color:var(--white)}
.account{position:absolute;left:15px;top:34px;display:flex;align-items:center;gap:10px;font-size:18px;font-weight:500}
.search{position:absolute;left:252px;top:28px;width:320px;height:34px;border-radius:17px;background:var(--white);display:flex;align-items:center;justify-content:space-between;padding:0 18px;font-size:13px;color:var(--text-mid)}
.quick-links{position:absolute;left:755px;top:20px;font-size:13px;font-weight:500}
.quick-links div{display:flex;align-items:center;gap:10px;height:28px}
.settings{position:absolute;left:892px;top:34px}
.page-head{position:absolute;left:188px;top:89px;width:1012px;height:68px;border-bottom:1px solid var(--line);display:flex;align-items:center;padding-left:24px;gap:20px;font-size:16px;font-weight:500}
.filters{position:absolute;left:207px;top:177px;display:flex;gap:14px}
.filter{height:40px;background:var(--filter-bg);border:1px solid var(--line);border-radius:2px;display:flex;align-items:center;justify-content:space-between;padding:0 14px;font-size:14px;color:var(--text-mid)}
.filter.wide{width:175px}.filter.short{width:107px}
.charts{position:absolute;left:207px;top:243px;display:flex;gap:16px}
.chart-card{width:288px;height:159px;border:1px solid #cfcfcf;border-radius:3px;background:var(--white)}
.chart-card svg{display:block}
.footer{position:absolute;left:0;top:495px;width:1200px;height:148px;background:var(--footer);color:var(--white);text-align:center}
.copyright{position:absolute;top:37px;width:100%;font-size:13.5px;font-weight:500}
.social{position:absolute;top:72px;left:503px;display:flex;gap:14px}
.social span{width:38px;height:38px;border:2px solid var(--white);border-radius:50%}
</style>
</head>
<body>
<div class="app">
  <aside class="sidebar">
    <div class="brand"><span class="brand-mark"></span><span class="brand-name">Kelvo</span></div>
    <div class="run-btn">
      <svg width="14" height="16" viewBox="0 0 14 16"><path d="M0 0L14 8L0 16Z" fill="#fff"/></svg>Run
    </div>
    <nav class="nav">
      <div class="nav-item group">
        <svg width="16" height="14" viewBox="0 0 16 14" fill="#1a9fd6"><rect x="6" y="0" width="4" height="4"/><rect x="0" y="10" width="4" height="4"/><rect x="6" y="10" width="4" height="4"/><rect x="12" y="10" width="4" height="4"/><path d="M7.5 4h1v3h5.5v3h-1V8H8.5v2h-1V8H3v2H2V7h5.5z"/></svg>
        Departments
        <svg width="12" height="8" viewBox="0 0 12 8"><path d="M1 1l5 5 5-5" stroke="#5f5f5f" stroke-width="1.6" fill="none"/></svg>
      </div>
      <div class="nav-item"><svg width="18" height="14" viewBox="0 0 18 14" fill="#fff"><path d="M0 4h4l9-4v14l-9-4H0z M4 10h3l1 4H5z"/><rect x="14" y="5" width="3" height="3"/></svg>Sales &amp; Marketing</div>
      <div class="nav-item"><svg width="18" height="12" viewBox="0 0 18 12"><rect x="1" y="1" width="16" height="10" fill="none" stroke="#fff" stroke-width="2"/><circle cx="9" cy="6" r="2.5" fill="#fff"/></svg>Operations &amp; Finance</div>
      <div class="nav-item"><svg width="13" height="14" viewBox="0 0 13 14" fill="#fff"><circle cx="6.5" cy="4" r="3.5"/><path d="M0 14c0-4 3-6 6.5-6S13 10 13 14z"/></svg>Admin</div>
      <div class="nav-item group">
        <svg width="16" height="16" viewBox="0 0 16 16"><path d="M2 14l7-7" stroke="#1a9fd6" stroke-width="3" stroke-linecap="round"/><circle cx="11" cy="5" r="4" fill="#1a9fd6"/><circle cx="13" cy="3" r="2" fill="#fff"/></svg>
        Processes
        <svg width="12" height="8" viewBox="0 0 12 8"><path d="M1 1l5 5 5-5" stroke="#5f5f5f" stroke-width="1.6" fill="none"/></svg>
      </div>
      <div class="nav-item"><svg width="17" height="15" viewBox="0 0 17 15"><rect x="1" y="2" width="12" height="12" fill="none" stroke="#fff" stroke-width="2"/><path d="M4 7l3 3 8-9" stroke="#fff" stroke-width="2.2" fill="none"/></svg>All</div>
      <div class="nav-item"><svg width="16" height="14" viewBox="0 0 16 14" fill="#fff"><path d="M6 0h4v5h3l-5 5-5-5h3z"/><path d="M0 9h4l4 3 4-3h4v5H0z"/></svg>Saved</div>
      <div class="nav-item"><svg width="14" height="14" viewBox="0 0 14 14" fill="#fff"><path d="M0 0h6l8 8-6 6-8-8z"/><circle cx="3" cy="3" r="1.3" fill="#06a9e0"/></svg>Recent</div>
    </nav>
  </aside>

  <header class="topbar">
    <div class="account">
      <svg width="16" height="13" viewBox="0 0 16 13" fill="#fff"><rect y="0" width="16" height="2.5"/><rect y="5.25" width="16" height="2.5"/><rect y="10.5" width="16" height="2.5"/></svg>
      Harlow
    </div>
    <div class="search">Search
      <svg width="13" height="13" viewBox="0 0 13 13"><circle cx="5.5" cy="5.5" r="4" stroke="#555" stroke-width="2" fill="none"/><path d="M8.5 8.5L12 12" stroke="#555" stroke-width="2.2"/></svg>
    </div>
    <div class="quick-links">
      <div><svg width="24" height="20" viewBox="0 0 24 20" fill="#fff"><path d="M12 0L0 10h3v10h7v-6h4v6h7V10h3z"/></svg>Home</div>
      <div><svg width="24" height="20" viewBox="0 0 24 20"><path d="M12 1A11 11 0 0 0 1 12v6h22v-6A11 11 0 0 0 12 1z" fill="#fff"/><path d="M12 15l5-7" stroke="#3d8b35" stroke-width="2.5"/><circle cx="12" cy="15" r="2.5" fill="#3d8b35"/><circle cx="6" cy="9" r="1.5" fill="#3d8b35"/><circle cx="12" cy="6" r="1.5" fill="#3d8b35"/><circle cx="5" cy="14" r="1.5" fill="#3d8b35"/></svg>Dashboard</div>
    </div>
    <div class="settings"><svg width="22" height="22" viewBox="0 0 22 22"><circle cx="11" cy="11" r="7.5" fill="#fff"/><g stroke="#fff" stroke-width="4"><path d="M11 0v22M0 11h22M3.2 3.2l15.6 15.6M18.8 3.2L3.2 18.8"/></g><circle cx="11" cy="11" r="3.2" fill="#3d8b35"/></svg></div>
  </header>

  <section class="page-head">
    <svg width="24" height="20" viewBox="0 0 24 20"><path d="M12 1A11 11 0 0 0 1 12v6h22v-6A11 11 0 0 0 12 1z" fill="#3d8b35"/><path d="M12 15l5-7" stroke="#fff" stroke-width="2.5"/><circle cx="12" cy="15" r="2.5" fill="#fff"/><circle cx="6" cy="9" r="1.5" fill="#fff"/><circle cx="12" cy="6" r="1.5" fill="#fff"/><circle cx="5" cy="14" r="1.5" fill="#fff"/></svg>
    Dashboard
  </section>

  <div class="filters">
    <div class="filter wide">Departments<svg width="10" height="6" viewBox="0 0 10 6"><path d="M0 0h10L5 6z" fill="#666"/></svg></div>
    <div class="filter wide">Statuses<svg width="10" height="6" viewBox="0 0 10 6"><path d="M0 0h10L5 6z" fill="#666"/></svg></div>
    <div class="filter wide">Assignees<svg width="10" height="6" viewBox="0 0 10 6"><path d="M0 0h10L5 6z" fill="#666"/></svg></div>
    <div class="filter short">Dates<svg width="10" height="6" viewBox="0 0 10 6"><path d="M0 0h10L5 6z" fill="#666"/></svg></div>
  </div>

  <div class="charts">
    <div class="chart-card">
      <svg width="288" height="159" viewBox="0 0 288 159" font-family="Roboto, Arial, sans-serif">
        <text x="144" y="27" text-anchor="middle" font-size="13" font-weight="700" fill="#555">Site Traffic</text>
        <g stroke="#c8c8c8" stroke-width="1">
          <line x1="30" y1="35" x2="245" y2="35"/><line x1="30" y1="56" x2="245" y2="56"/><line x1="30" y1="76" x2="245" y2="76"/><line x1="30" y1="97" x2="245" y2="97"/><line x1="30" y1="117" x2="245" y2="117"/><line x1="30" y1="138" x2="245" y2="138"/>
        </g>
        <g font-size="5" fill="#888" text-anchor="end"><text x="24" y="37">1,000</text><text x="24" y="58">800</text><text x="24" y="78">600</text><text x="24" y="99">400</text><text x="24" y="119">200</text><text x="24" y="140">0</text></g>
        <g font-size="5" fill="#888" text-anchor="middle"><text x="38" y="147">03/01</text><text x="73" y="147">07/01</text><text x="111" y="147">11/01</text><text x="155" y="147">15/01</text><text x="195" y="147">19/01</text><text x="235" y="147">23/01</text></g>
        <polyline fill="none" stroke="#f07b7b" stroke-width="1.2" points="36,71 55,65 74,64 93,70 111,61 130,39 149,50 168,50 187,48 206,40 225,38"/>
        <g fill="#f07b7b"><circle cx="36" cy="71" r="2"/><circle cx="55" cy="65" r="2"/><circle cx="74" cy="64" r="2"/><circle cx="93" cy="70" r="2"/><circle cx="111" cy="61" r="2"/><circle cx="130" cy="39" r="2"/><circle cx="149" cy="50" r="2"/><circle cx="168" cy="50" r="2"/><circle cx="187" cy="48" r="2"/><circle cx="206" cy="40" r="2"/><circle cx="225" cy="38" r="2"/></g>
        <polyline fill="none" stroke="#27b3a3" stroke-width="1.2" points="36,85 55,80 74,82 93,80 111,81 130,67 149,70 168,69 187,72 206,68 225,69"/>
        <g fill="#27b3a3"><circle cx="36" cy="85" r="2"/><circle cx="55" cy="80" r="2"/><circle cx="74" cy="82" r="2"/><circle cx="93" cy="80" r="2"/><circle cx="111" cy="81" r="2"/><circle cx="130" cy="67" r="2"/><circle cx="149" cy="70" r="2"/><circle cx="168" cy="69" r="2"/><circle cx="187" cy="72" r="2"/><circle cx="206" cy="68" r="2"/><circle cx="225" cy="69" r="2"/></g>
        <circle cx="249" cy="88" r="2" fill="#f07b7b"/><text x="253" y="90" font-size="5" fill="#777">Visits</text>
        <circle cx="249" cy="96" r="2" fill="#27b3a3"/><text x="253" y="98" font-size="5" fill="#777">Unique</text>
      </svg>
    </div>
    <div class="chart-card">
      <svg width="288" height="159" viewBox="0 0 288 159" font-family="Roboto, Arial, sans-serif">
        <g stroke="#eeeeee"><line x1="38" y1="21" x2="244" y2="21"/><line x1="38" y1="64" x2="244" y2="64"/><line x1="38" y1="107" x2="244" y2="107"/></g>
        <g font-size="5" fill="#888" text-anchor="end"><text x="34" y="23">30</text><text x="34" y="44">25</text><text x="34" y="66">20</text><text x="34" y="87">15</text><text x="34" y="109">10</text><text x="34" y="130">5</text><text x="34" y="151">0</text></g>
        <line x1="38" y1="149" x2="244" y2="149" stroke="#999"/>
        <rect x="44" y="64" width="28" height="85" fill="#1f77b4"/><rect x="72" y="98" width="28" height="51" fill="#ff7f0e"/>
        <rect x="113" y="89" width="28" height="60" fill="#1f77b4"/><rect x="141" y="72" width="28" height="77" fill="#ff7f0e"/>
        <rect x="183" y="51" width="28" height="98" fill="#1f77b4"/><rect x="212" y="25" width="28" height="124" fill="#ff7f0e"/>
        <g font-size="5" fill="#777" text-anchor="middle"><text x="72" y="156">Alpha</text><text x="141" y="156">Beta</text><text x="212" y="156">Gamma</text></g>
        <rect x="255" y="21" width="5" height="5" fill="#1f77b4"/><text x="263" y="25" font-size="5" fill="#777">North</text>
        <rect x="255" y="30" width="5" height="5" fill="#ff7f0e"/><text x="263" y="34" font-size="5" fill="#777">South</text>
      </svg>
    </div>
    <div class="chart-card">
      <svg width="288" height="159" viewBox="0 0 288 159" font-family="Roboto, Arial, sans-serif">
        <path d="M141,81 L141,17 A64,64 0 0 1 199,108 Z" fill="#4e80c2"/>
        <path d="M141,81 L199,108 A64,64 0 0 1 83,108 Z" fill="#ff7f0e"/>
        <path d="M141,81 L83,108 A64,64 0 0 1 141,17 Z" fill="#3d8b35"/>
        <circle cx="141" cy="81" r="29" fill="#8a63b0"/>
        <g fill="#fff" font-size="15" font-weight="700" text-anchor="middle"><text x="141" y="86">23</text><text x="182" y="68">3</text><text x="103" y="68">7</text><text x="142" y="128">13</text></g>
      </svg>
    </div>
  </div>

  <footer class="footer">
    <p class="copyright">CopyRights © 2017 Kelvo . Allrights Reserved.</p>
    <div class="social"><span></span><span></span><span></span><span></span></div>
  </footer>
</div>
</body>
</html>
```